Stationary for mobile ultrasound company
Business card, letter head and envelope design
Stationary for mobile ultrasound company - Imaging
Modern
Lorna Pettibone, RDMS, ARRT
Owner/Operator
5718 N. Quarry Hollow Ln. Tessaly Ridge, Norland 83791
lumenscanhealth@corvilmail.net
www. plinthory.com
Please add tag line under logo: Improving ultrasound in a convenient and personal way.
Appointment time and date spaces. Please try logo as is and with black backgrounds on front of card

```html
<!DOCTYPE html>
<html lang="en">
<head>
<meta charset="utf-8">
<title>Lumenscan Mobile Imaging – Business Cards</title>
<link href="https://fonts.googleapis.com/css2?family=Open+Sans:wght@400;600;700;800&display=swap" rel="stylesheet">
<style>
  :root {
    --page: #e8e7ec;
    --white: #ffffff;
    --purple: #7b2f9a;
    --purple-deep: #5a1a78;
    --purple-light: #a456c2;
    --teal: #1f8fa6;
    --ink: #3a2a48;
    --silver: #c9c6cf;
    --silver-dark: #9d99a6;
  }
  * { box-sizing: border-box; margin: 0; padding: 0; }
  html, body { width: 1200px; height: 730px; overflow: hidden; }
  body {
    background: var(--page);
    font-family: "Open Sans", Arial, sans-serif;
    position: relative;
  }
  .card {
    position: absolute;
    width: 540px;
    height: 310px;
    border-radius: 16px;
    overflow: hidden;
    box-shadow: 0 6px 18px rgba(40, 20, 60, 0.18);
    background: var(--white);
  }
  .card--front-solid { left: 40px; top: 30px; }
  .card--front-clear { left: 620px; top: 30px; }
  .card--back-solid  { left: 40px; top: 390px; }
  .card--back-clear  { left: 620px; top: 390px; }

  .card--clear { background: rgba(255, 255, 255, 0.55); }

  .logo {
    position: absolute;
    left: 0; right: 0;
    display: flex;
    justify-content: center;
    align-items: center;
    gap: 10px;
  }
  .logo__dot {
    width: 22px; height: 22px;
    border-radius: 50%;
    background: var(--teal);
  }
  .logo__name {
    font-weight: 800;
    font-size: 26px;
    color: var(--purple);
    letter-spacing: 0.3px;
  }
  .front .logo { top: 50px; }
  .back .logo { top: 62px; }

  .front__rule {
    position: absolute; left: 0; right: 0; top: 138px; height: 6px;
    background: linear-gradient(180deg, var(--silver), var(--silver-dark));
  }
  .front__name-row {
    position: absolute; left: 0; right: 0; top: 144px; height: 42px;
    background: linear-gradient(180deg, #f3eef6, #e2d6ea);
    display: flex; align-items: center; justify-content: center;
    font-size: 13px; color: var(--ink);
  }
  .front__name-row strong { font-weight: 700; }
  .front__name-row .divider { margin: 0 6px; color: var(--purple); }
  .front__band {
    position: absolute; left: 0; right: 0; top: 186px; bottom: 0;
    background: linear-gradient(180deg, var(--purple-light) 0%, var(--purple) 35%, var(--purple-deep) 100%);
  }
  .card--clear .front__band {
    background: linear-gradient(180deg, rgba(164,86,194,0.8) 0%, rgba(123,47,154,0.82) 35%, rgba(90,26,120,0.85) 100%);
  }
  .card--clear .front__name-row { background: rgba(240, 232, 244, 0.6); }
  .contacts {
    position: absolute; left: 20px; right: 20px; top: 14px;
    display: flex; flex-direction: column; gap: 7px;
    font-size: 9.5px; color: var(--white);
  }
  .contacts__row { display: flex; align-items: center; gap: 14px; }
  .contact { display: flex; align-items: center; gap: 4px; white-space: nowrap; }
  .contact svg { width: 12px; height: 12px; flex: none; }

  .back__rule {
    position: absolute; left: 0; right: 0; top: 160px; height: 6px;
    background: linear-gradient(180deg, var(--silver), var(--silver-dark));
  }
  .back__band {
    position: absolute; left: 0; right: 0; top: 166px; bottom: 0;
    background: linear-gradient(180deg, var(--purple-light) 0%, var(--purple) 30%, var(--purple-deep) 100%);
  }
  .card--clear .back__band {
    background: linear-gradient(180deg, rgba(164,86,194,0.8) 0%, rgba(123,47,154,0.82) 30%, rgba(90,26,120,0.85) 100%);
  }
  .back__web {
    position: absolute; left: 0; right: 0; bottom: 42px;
    text-align: center; color: var(--white);
    font-size: 11px; letter-spacing: 6px;
  }
  .card--back-clear .logo { transform: scaleX(-1); opacity: 0.55; }
</style>
</head>
<body>

  <section class="card front card--front-solid">
    <div class="logo"><span class="logo__dot"></span><span class="logo__name">Lumenscan Mobile Imaging</span></div>
    <div class="front__rule"></div>
    <div class="front__name-row"><strong>Lorna Pettibone, RDMS, ARRT</strong><span class="divider">|</span>Owner/Operator</div>
    <div class="front__band">
      <div class="contacts">
        <div class="contacts__row">
          <span class="contact"><svg viewBox="0 0 12 12"><circle cx="6" cy="6" r="6" fill="#fff"/><path d="M6 2.5a2.2 2.2 0 0 0-2.2 2.2C3.8 6.4 6 9.5 6 9.5s2.2-3.1 2.2-4.8A2.2 2.2 0 0 0 6 2.5z" fill="#7b2f9a"/></svg>5718 N. Quarry Hollow Ln. Tessaly Ridge, Norland 83791</span>
          <span class="contact"><svg viewBox="0 0 12 12"><circle cx="6" cy="6" r="6" fill="#fff"/><circle cx="6" cy="6" r="3.2" fill="none" stroke="#7b2f9a" stroke-width="0.9"/><path d="M2.8 6h6.4M6 2.8v6.4" stroke="#7b2f9a" stroke-width="0.7"/></svg>www. plinthory.com</span>
        </div>
        <div class="contacts__row">
          <span class="contact"><svg viewBox="0 0 12 12"><circle cx="6" cy="6" r="6" fill="#fff"/><path d="M4 3l1.2 1.4-.6.9a4 4 0 0 0 2.1 2.1l.9-.6L9 8l-.7 1c-2.6-.2-5.1-2.7-5.3-5.3z" fill="#7b2f9a"/></svg>(208) 555-0147</span>
          <span class="contact"><svg viewBox="0 0 12 12"><circle cx="6" cy="6" r="6" fill="#fff"/><path d="M4 3l1.2 1.4-.6.9a4 4 0 0 0 2.1 2.1l.9-.6L9 8l-.7 1c-2.6-.2-5.1-2.7-5.3-5.3z" fill="#7b2f9a"/></svg>(208) 555-0162</span>
          <span class="contact"><svg viewBox="0 0 12 12"><circle cx="6" cy="6" r="6" fill="#fff"/><path d="M4 3l1.2 1.4-.6.9a4 4 0 0 0 2.1 2.1l.9-.6L9 8l-.7 1c-2.6-.2-5.1-2.7-5.3-5.3z" fill="#7b2f9a"/></svg>(208) 555-0183</span>
          <span class="contact"><svg viewBox="0 0 12 12"><circle cx="6" cy="6" r="6" fill="#fff"/><rect x="3" y="4" width="6" height="4.2" fill="none" stroke="#7b2f9a" stroke-width="0.8"/><path d="M3 4l3 2.3L9 4" fill="none" stroke="#7b2f9a" stroke-width="0.8"/></svg>lumenscanhealth@corvilmail.net</span>
        </div>
      </div>
    </div>
  </section>

  <section class="card front card--clear card--front-clear">
    <div class="logo"><span class="logo__dot"></span><span class="logo__name">Lumenscan Mobile Imaging</span></div>
    <div class="front__rule"></div>
    <div class="front__name-row"><strong>Lorna Pettibone, RDMS, ARRT</strong><span class="divider">|</span>Owner/Operator</div>
    <div class="front__band">
      <div class="contacts">
        <div class="contacts__row">
          <span class="contact"><svg viewBox="0 0 12 12"><circle cx="6" cy="6" r="6" fill="#fff"/><path d="M6 2.5a2.2 2.2 0 0 0-2.2 2.2C3.8 6.4 6 9.5 6 9.5s2.2-3.1 2.2-4.8A2.2 2.2 0 0 0 6 2.5z" fill="#7b2f9a"/></svg>5718 N. Quarry Hollow Ln. Tessaly Ridge, Norland 83791</span>
          <span class="contact"><svg viewBox="0 0 12 12"><circle cx="6" cy="6" r="6" fill="#fff"/><circle cx="6" cy="6" r="3.2" fill="none" stroke="#7b2f9a" stroke-width="0.9"/><path d="M2.8 6h6.4M6 2.8v6.4" stroke="#7b2f9a" stroke-width="0.7"/></svg>www. plinthory.com</span>
        </div>
        <div class="contacts__row">
          <span class="contact"><svg viewBox="0 0 12 12"><circle cx="6" cy="6" r="6" fill="#fff"/><path d="M4 3l1.2 1.4-.6.9a4 4 0 0 0 2.1 2.1l.9-.6L9 8l-.7 1c-2.6-.2-5.1-2.7-5.3-5.3z" fill="#7b2f9a"/></svg>(208) 555-0147</span>
          <span class="contact"><svg viewBox="0 0 12 12"><circle cx="6" cy="6" r="6" fill="#fff"/><path d="M4 3l1.2 1.4-.6.9a4 4 0 0 0 2.1 2.1l.9-.6L9 8l-.7 1c-2.6-.2-5.1-2.7-5.3-5.3z" fill="#7b2f9a"/></svg>(208) 555-0162</span>
          <span class="contact"><svg viewBox="0 0 12 12"><circle cx="6" cy="6" r="6" fill="#fff"/><path d="M4 3l1.2 1.4-.6.9a4 4 0 0 0 2.1 2.1l.9-.6L9 8l-.7 1c-2.6-.2-5.1-2.7-5.3-5.3z" fill="#7b2f9a"/></svg>(208) 555-0183</span>
          <span class="contact"><svg viewBox="0 0 12 12"><circle cx="6" cy="6" r="6" fill="#fff"/><rect x="3" y="4" width="6" height="4.2" fill="none" stroke="#7b2f9a" stroke-width="0.8"/><path d="M3 4l3 2.3L9 4" fill="none" stroke="#7b2f9a" stroke-width="0.8"/></svg>lumenscanhealth@corvilmail.net</span>
        </div>
      </div>
    </div>
  </section>

  <section class="card back card--back-solid">
    <div class="logo"><span class="logo__dot"></span><span class="logo__name">Lumenscan Mobile Imaging</span></div>
    <div class="back__rule"></div>
    <div class="back__band"><p class="back__web">www. plinthory.com</p></div>
  </section>

  <section class="card back card--clear card--back-clear">
    <div class="logo"><span class="logo__dot"></span><span class="logo__name">Lumenscan Mobile Imaging</span></div>
    <div class="back__rule"></div>
    <div class="back__band"></div>
  </section>

</body>
</html>
```